Realtor Business Card

To create a new cutting edge classic 2-sided business card. Including personal logo, company logo, and contact info. Possibly including a headshot and slogon.
"4 Generations of Victoria Real Estate Service"
The company's color is dark blue. My logo color is green as indicated on the attached files.
Company logos on one side (Calder Ridge Realty and Ashgrove Land Office) personal info and logo on the other.

```html
<!DOCTYPE html>
<html lang="en">
<head>
<meta charset="utf-8">
<title>Owen Hartley – Business Card</title>
<link rel="stylesheet" href="https://fonts.googleapis.com/css2?family=Cinzel:wght@400&family=Open+Sans:wght@400&family=Pinyon+Script&display=swap">
<style>
  :root {
    --bg: #8f8f8f;
    --olive: #93993e;
    --olive-light: #a3a95a;
    --paper: #ebebeb;
    --ink: #555555;
    --ink-soft: #777777;
    --white: #ffffff;
    --brick-dark: #5e3a2e;
    --brick: #8a5a48;
  }
  * { margin: 0; padding: 0; box-sizing: border-box; }
  html, body { width: 1200px; height: 1200px; overflow: hidden; }
  body { background: var(--bg); position: relative; font-family: "Open Sans", sans-serif; }

  .card {
    position: absolute;
    left: 227px;
    width: 746px;
    height: 435px;
    border-radius: 24px;
    overflow: hidden;
  }

  /* Front */
  .card-front { top: 108px; background: var(--olive); }
  .monogram-watermark {
    position: absolute;
    left: -20px;
    top: -40px;
    font-family: "Cinzel", serif;
    font-size: 560px;
    line-height: 1;
    color: var(--olive-light);
    letter-spacing: -40px;
    white-space: nowrap;
  }
  .partner-marks {
    position: absolute;
    right: 44px;
    bottom: 62px;
    display: flex;
    align-items: center;
    gap: 24px;
  }
  .partner { display: flex; align-items: center; gap: 8px; color: var(--white); font-family: "Cinzel", serif; font-size: 17px; line-height: 1.15; }
  .partner-square { width: 14px; height: 14px; background: var(--white); flex: none; }

  /* Back */
  .card-back { top: 599px; background: var(--paper); display: flex; }
  .info-panel { width: 384px; height: 100%; position: relative; text-align: center; }
  .personal-mark {
    position: absolute; left: 161px; top: 60px;
    width: 62px; height: 62px; border-radius: 6px; background: var(--olive);
  }
  .agent-name {
    position: absolute; left: 0; right: 0; top: 132px;
    font-family: "Cinzel", serif; font-size: 32px; color: var(--olive); letter-spacing: 1px; font-weight: 400;
  }
  .agent-title {
    position: absolute; left: 0; right: 0; top: 178px;
    font-size: 12.5px; color: var(--ink); letter-spacing: 0.3px;
  }
  .agent-title::before {
    content: ""; position: absolute; left: 50px; right: 50px; top: -6px; height: 1px; background: var(--olive);
  }
  .slogan {
    position: absolute; left: 0; right: 0; top: 206px;
    font-family: "Pinyon Script", cursive; font-size: 19px; color: var(--ink-soft);
  }
  .contact-list { position: absolute; left: 0; right: 0; top: 268px; list-style: none; }
  .contact-list li {
    height: 24px; display: flex; justify-content: center; align-items: center; gap: 6px;
    font-size: 15.5px; color: var(--ink);
  }
  .contact-list svg { width: 13px; height: 13px; fill: var(--olive); flex: none; }
  .divider { position: absolute; left: 107px; width: 170px; top: 376px; height: 1px; background: var(--olive); opacity: 0.6; }
  .address { position: absolute; left: 0; right: 0; top: 391px; font-size: 13px; color: var(--ink); }

  .portrait-area {
    flex: 1; height: 100%;
    background: linear-gradient(160deg, var(--brick) 0%, var(--brick-dark) 70%, #2b2a30 100%);
  }
</style>
</head>
<body>

<section class="card card-front">
  <div class="monogram-watermark" aria-hidden="true">OH</div>
  <div class="partner-marks">
    <div class="partner"><span class="partner-square"></span><span>Calder Ridge<br>Realty</span></div>
    <div class="partner"><span class="partner-square"></span><span>Ashgrove<br>Land Office</span></div>
  </div>
</section>

<section class="card card-back">
  <div class="info-panel">
    <div class="personal-mark" aria-hidden="true"></div>
    <h1 class="agent-name">Owen Hartley</h1>
    <p class="agent-title">REAL ESTATE PROFESSIONAL - VICTORIA, BC</p>
    <p class="slogan">4 Generations of Victoria Real Estate Services</p>
    <ul class="contact-list">
      <li><svg viewBox="0 0 16 16"><path d="M4 0h8a1 1 0 0 1 1 1v14a1 1 0 0 1-1 1H4a1 1 0 0 1-1-1V1a1 1 0 0 1 1-1zm1 2v10h6V2z"/></svg>(250) 555-0142</li>
      <li><svg viewBox="0 0 16 16"><path d="M3.6 1l2.6 3.2-1.5 1.8c.9 2 2.4 3.5 4.3 4.3l1.8-1.5L14 11.4 12.6 14C7 14 2 9 2 3.4z"/></svg>(250) 555.0187</li>
      <li><svg viewBox="0 0 16 16"><path d="M1 3h14v10H1zm1.5 1.2v.4L8 8.6l5.5-4v-.4z"/></svg>owen@owenhartley.com</li>
      <li><svg viewBox="0 0 16 16"><path d="M8 1a7 7 0 1 0 0 14A7 7 0 0 0 8 1zm0 1.5c.8.8 1.5 2.4 1.7 4.5H6.3C6.5 4.9 7.2 3.3 8 2.5zM2.6 7h2.2c.1-1.7.5-3.1 1.1-4.1A5.5 5.5 0 0 0 2.6 7zm0 2a5.5 5.5 0 0 0 3.3 4.1c-.6-1-1-2.4-1.1-4.1zm3.7 0h3.4c-.2 2.1-.9 3.7-1.7 4.5-.8-.8-1.5-2.4-1.7-4.5zm4.9 0c-.1 1.7-.5 3.1-1.1 4.1A5.5 5.5 0 0 0 13.4 9zm2.2-2a5.5 5.5 0 0 0-3.3-4.1c.6 1 1 2.4 1.1 4.1z"/></svg>owenhartley.com</li>
    </ul>
    <div class="divider"></div>
    <p class="address">2210 Alder Street, Victoria, BC V8V 1A1</p>
  </div>
  <div class="portrait-area" role="img" aria-label="Headshot of the agent in a dark blazer and white shirt against a brick wall"></div>
</section>

</body>
</html>
```